Verdant Ledger - Paid Surveys publisher portal

• Homepage
• Blank Sub Page (Where content goes in between the header/footer)
• Publisher Application Page, complete with Form
• Survey Wall page

Sites that are in a similar vertical that have interesting designs:
mobrivex.com
tandulo.com
vorql.com
pim.ox

This is a business-to-business site, and needs to have this type of feel to it. Focus on generating revenue, offer completion, paid surveys is the market.

Format: HTML/CSS

Link to current version of application, and form:
https://quorbit.travenlo.com
https://quorbit.travenlo.com/apply
https://quorbit.travenlo.com/panel/4/mirvak_user

Please note that we are changing the brand of this project, the name will be determined shortly but everything else remains. It will likely be Verdant Ledger instead of Quorbit. We will confirm.

Industry/Entity Type

Market Research

Coding

Coded - Design and coding required

Number of Pages Required

4 page

Font styles to use
Sans Serif

Colors

Designer to choose colors to be used in the design.

```html
<!DOCTYPE html>
<html lang="en">
<head>
<meta charset="utf-8">
<title>Quorbit – Paid Surveys Publisher Portal</title>
<link href="https://fonts.googleapis.com/css2?family=Poppins:wght@300;400;500;600&display=swap" rel="stylesheet">
<style>
:root{
  --blue:#1b8fd6;
  --blue-dark:#1d6fb8;
  --red:#e8322b;
  --ink:#222;
  --muted:#666;
  --light:#f4f4f4;
  --footer:#2a2a2a;
  --white:#fff;
}
*{margin:0;padding:0;box-sizing:border-box}
html,body{width:1200px;height:3364px;overflow:hidden}
body{position:relative;font-family:'Poppins',Arial,sans-serif;color:var(--ink);background:var(--white)}

/* header */
.site-header{position:absolute;left:0;top:0;width:1200px;height:99px;background:var(--white)}
.brand{position:absolute;left:86px;top:22px;display:flex;align-items:center;gap:14px}
.brand-dot{width:54px;height:54px;border-radius:50%;background:var(--red)}
.brand-name{font-size:28px;font-weight:500;color:#333}
.nav{position:absolute;top:41px;font-size:13px;font-weight:500;color:#333;white-space:nowrap}
.nav.active{color:var(--red)}
.search-btn{position:absolute;left:1063px;top:24px;width:50px;height:50px;border:2px solid var(--red);border-radius:50%}

/* hero */
.hero{position:absolute;left:0;top:99px;width:1200px;height:552px;background:linear-gradient(100deg,#3b3f44 0%,#5a5e62 45%,#7c7a76 70%,#4d4f52 100%)}
.hero-shade{position:absolute;inset:0;background:linear-gradient(90deg,rgba(0,0,0,.45),rgba(0,0,0,0) 60%)}
.hero-title{position:absolute;left:101px;top:180px;font-size:54px;font-weight:500;color:var(--white)}
.hero-sub{position:absolute;left:103px;top:272px;font-size:16px;font-weight:600;line-height:31px;color:var(--white);text-transform:uppercase}
.btn-ghost{position:absolute;display:flex;align-items:center;justify-content:center;border:2px solid var(--white);border-radius:24px;color:var(--white);font-weight:500}
.hero-arrow{position:absolute;top:259px;width:36px;height:36px;border:2px solid var(--white);border-radius:50%}

/* stats */
.stats{position:absolute;left:0;top:651px;width:1200px;height:145px;display:flex}
.stat{flex:1;color:var(--white);text-align:center;padding-top:28px}
.stat-num{font-size:44px;font-weight:400;line-height:52px}
.stat-label{font-size:15px;font-weight:300}

/* welcome */
.welcome-photo{position:absolute;left:159px;top:861px;width:500px;height:388px;background:linear-gradient(160deg,#c9ccd0,#8d939b 60%,#3b3d44)}
.welcome-card{position:absolute;left:496px;top:1005px;width:545px;height:334px;background:var(--white);box-shadow:0 2px 12px rgba(0,0,0,.18);padding:36px 44px}
.welcome-card h2{font-size:28px;font-weight:400;color:var(--blue)}
.welcome-card p{margin-top:14px;font-size:11.5px;line-height:29px;color:var(--muted)}
.btn-outline{display:inline-flex;align-items:center;justify-content:center;border:1.5px solid var(--blue);color:var(--blue);font-size:14px;width:112px;height:36px;margin-top:20px}

/* section titles */
.section-title{position:absolute;left:0;width:1200px;text-align:center;font-size:33px;font-weight:400;color:var(--blue)}
.section-sub{position:absolute;left:0;width:1200px;text-align:center;font-size:12px;color:var(--muted)}

/* services */
.services{position:absolute;left:0;top:1402px;width:1200px;height:442px;background:var(--light)}
.service{position:absolute;top:168px;width:300px;text-align:center}
.service svg{display:block;margin:0 auto}
.service h3{font-size:20px;font-weight:400;color:#333;margin-top:20px}
.service p{font-size:12px;line-height:26px;color:var(--muted);margin-top:10px}

/* news */
.news-card{position:absolute;top:1985px;width:330px;height:498px;background:var(--white);box-shadow:0 1px 6px rgba(0,0,0,.18)}
.news-img{height:224px}
.news-body{padding:20px 22px 0}
.news-cat{font-size:18px;font-weight:400;color:var(--blue)}
.news-title{font-size:13px;font-weight:500;line-height:25px;margin-top:12px;color:#333;white-space:nowrap}
.news-text{font-size:11px;line-height:26px;color:var(--muted);margin-top:10px;height:78px;overflow:hidden}
.news-foot{position:absolute;left:0;bottom:0;width:100%;height:54px;border-top:1px solid #e2e2e2;display:flex;justify-content:space-between;align-items:center;padding:0 16px;font-size:13px;color:var(--blue)}

/* banner */
.banner{position:absolute;left:0;top:2546px;width:1200px;height:406px;background:linear-gradient(120deg,#1583cd,#22a3e2 55%,#38b6ec)}
.banner-art{position:absolute;left:640px;top:0;width:560px;height:406px;background:radial-gradient(circle at 30% 60%,rgba(255,255,255,.55),rgba(255,255,255,0) 45%),radial-gradient(circle at 75% 40%,rgba(255,255,255,.25),rgba(255,255,255,0) 40%)}
.banner h2{position:absolute;left:85px;top:83px;font-size:32px;font-weight:500;color:var(--white)}
.banner p{position:absolute;left:87px;top:148px;width:430px;font-size:11.5px;line-height:27px;color:var(--white)}

/* footer */
.site-footer{position:absolute;left:0;top:2952px;width:1200px;height:412px;background:var(--footer);color:#ddd}
.foot-col{position:absolute;top:70px}
.foot-col h4{font-size:19px;font-weight:400;color:var(--white);text-transform:uppercase;margin-bottom:22px;white-space:nowrap}
.foot-list{font-size:13.5px;line-height:30px;color:#ddd;list-style:none}
.contact-lines{font-size:14px;line-height:18px}
.contact-lines dt{text-transform:uppercase}
.contact-lines dd{margin-bottom:22px}
.email-field{position:absolute;left:830px;top:116px;width:262px;height:36px;background:var(--white);border-radius:3px;font-size:10px;color:#444;padding:11px 14px;text-transform:uppercase}
.subscribe{position:absolute;left:830px;top:163px;width:123px;height:34px;background:var(--blue);color:var(--white);font-size:12px;display:flex;align-items:center;justify-content:center;text-transform:uppercase}
.social{position:absolute;top:226px;width:36px;height:36px;border:2px solid var(--white);border-radius:50%}
.copyright{position:absolute;left:0;top:370px;width:1200px;text-align:center;font-size:13px;color:#ddd}
</style>
</head>
<body>

<header class="site-header">
  <div class="brand"><span class="brand-dot"></span><span class="brand-name">Quorbit</span></div>
  <span class="nav active" style="left:518px">Home</span>
  <span class="nav" style="left:607px">About Us</span>
  <span class="nav" style="left:717px">Services</span>
  <span class="nav" style="left:820px">Faq</span>
  <span class="nav" style="left:897px">News</span>
  <span class="nav" style="left:982px">Contact Us</span>
  <span class="search-btn">
    <svg width="46" height="46" viewBox="0 0 46 46"><circle cx="22" cy="22" r="5" fill="none" stroke="#e8322b" stroke-width="2"/><line x1="26" y1="26" x2="29" y2="29" stroke="#e8322b" stroke-width="2"/></svg>
  </span>
</header>

<section class="hero" role="img" aria-label="Photo of smiling colleagues in an office">
  <div class="hero-shade"></div>
  <h1 class="hero-title">Quorbit</h1>
  <p class="hero-sub">Sed ut perspiciatis unde omnis iste natus error<br>sit voluptatem accusantium</p>
  <a class="btn-ghost" style="left:105px;top:356px;width:140px;height:45px;font-size:15px">Read More</a>
  <span class="hero-arrow" style="left:40px"><svg width="32" height="32" viewBox="0 0 32 32"><path d="M18 10l-6 6 6 6" fill="none" stroke="#fff" stroke-width="2"/></svg></span>
  <span class="hero-arrow" style="left:1121px"><svg width="32" height="32" viewBox="0 0 32 32"><path d="M14 10l6 6-6 6" fill="none" stroke="#fff" stroke-width="2"/></svg></span>
</section>

<section class="stats">
  <div class="stat" style="background:#19a7dc"><div class="stat-num">100</div><div class="stat-label">Sed ut perspiciatis</div></div>
  <div class="stat" style="background:#1b9ad5"><div class="stat-num">80+</div><div class="stat-label">Sed ut perspiciatis</div></div>
  <div class="stat" style="background:#1e8bcc"><div class="stat-num">1500</div><div class="stat-label">Sed ut perspiciatis</div></div>
  <div class="stat" style="background:#217cc2"><div class="stat-num">180</div><div class="stat-label">Sed ut perspiciatis</div></div>
  <div class="stat" style="background:#246eb9"><div class="stat-num">250</div><div class="stat-label">Sed ut perspiciatis</div></div>
  <div class="stat" style="background:#2861b0"><div class="stat-num">50+</div><div class="stat-label">Sed ut perspiciatis</div></div>
</section>

<div class="welcome-photo" role="img" aria-label="Photo of a business team standing together"></div>
<article class="welcome-card">
  <h2>Welcome to Quorbit</h2>
  <p>Sed ut perspiciatis unde omnis iste natus error sit voluptatem accusantium doloremque laudantium, totam rem aperiam, eaque ipsa quae ab illo inventore veritatis et qu asi architecto beatae vitae dicta sunt explicabo. Nemo enim ipsam voluptatem qu ia voluptas sit aspernatur aut odit aut fugit, sed quia consequuntur magni dolores eos qui ratione voluptatem sequi nesciunt.</p>
  <a class="btn-outline">Read More</a>
</article>

<section class="services">
  <h2 class="section-title" style="top:36px">Our Services</h2>
  <p class="section-sub" style="top:88px">Sed ut perspiciatis unde omnis iste natus error sit voluptatem accusantium dolorem que laudantium, totam rem aperiam</p>
  <div class="service" style="left:97px">
    <svg width="80" height="80" viewBox="0 0 80 80" fill="none" stroke-width="3">
      <rect x="10" y="14" width="12" height="58" stroke="#2a6cb5"/><rect x="26" y="30" width="12" height="42" stroke="#2a6cb5"/><rect x="42" y="42" width="12" height="30" stroke="#2a6cb5"/>
      <path d="M14 22l22 12 14 10 18 14" stroke="#e8322b"/><path d="M60 58h10v-10" stroke="#e8322b"/>
    </svg>
    <h3>Sed ut perspiciatis</h3>
    <p>Sed ut perspiciatis unde omnis iste natus error<br>sit voluptatem accusantium dolorem que lauda<br>ntium, totam rem aperiam</p>
  </div>
  <div class="service" style="left:449px">
    <svg width="80" height="80" viewBox="0 0 80 80" fill="none" stroke-width="3">
      <circle cx="38" cy="44" r="28" stroke="#2a6cb5"/><circle cx="38" cy="44" r="17" stroke="#2a6cb5"/><circle cx="38" cy="44" r="6" stroke="#e8322b"/>
      <path d="M28 8h20l-4 8H32z" stroke="#2a6cb5"/><path d="M42 48l22 22" stroke="#e8322b"/>
    </svg>
    <h3>Sed ut perspiciatis</h3>
    <p>Sed ut perspiciatis unde omnis iste natus error<br>sit voluptatem accusantium dolorem que lauda<br>ntium, totam rem aperiam</p>
  </div>
  <div class="service" style="left:799px">
    <svg width="80" height="80" viewBox="0 0 80 80" fill="none" stroke-width="3">
      <path d="M70 10C52 12 38 24 30 44l8 8c20-8 32-22 32-42z" stroke="#2a6cb5"/><circle cx="52" cy="28" r="5" stroke="#2a6cb5"/>
      <path d="M30 44l-12-2 10-12h12M38 52l2 12 12-10V42" stroke="#2a6cb5"/><path d="M24 56L10 70M28 62l-8 8" stroke="#e8322b"/>
    </svg>
    <h3>Sed ut perspiciatis</h3>
    <p>Sed ut perspiciatis unde omnis iste natus error<br>sit voluptatem accusantium dolorem que lauda<br>ntium, totam rem aperiam</p>
  </div>
</section>

<h2 class="section-title" style="top:1872px">Latest News</h2>
<p class="section-sub" style="top:1926px">Sed ut perspiciatis unde omnis iste natus error sit voluptatem accusantium dolorem que laudantium, totam rem aperiam</p>

<article class="news-card" style="left:85px">
  <div class="news-img" role="img" aria-label="Photo of a presenter speaking to a seated group" style="background:linear-gradient(150deg,#9a8f84,#c8b9a6 50%,#6c655f)"></div>
  <div class="news-body">
    <h3 class="news-cat">Case Study</h3>
    <p class="news-title">Nemo enim ipsam voluptatem quia volup-<br>tas sit aspernatur aut odit</p>
    <p class="news-text">Sed ut perspiciatis unde omnis iste natus error sit vol uptatem accusantium doloremque laudantium, archi tecto beatae vitae dicta sunt</p>
  </div>
  <div class="news-foot"><span>03 Sep 2018</span><span>Read More</span></div>
</article>
<article class="news-card" style="left:433px">
  <div class="news-img" role="img" aria-label="Photo of an audience raising hands at a seminar" style="background:linear-gradient(150deg,#c5c9d6,#8e94a6 55%,#4b4f5d)"></div>
  <div class="news-body">
    <h3 class="news-cat">Generating Revenue</h3>
    <p class="news-title">Nemo enim ipsam voluptatem quia volup-<br>tas sit aspernatur aut odit</p>
    <p class="news-text">Sed ut perspiciatis unde omnis iste natus error sit vol uptatem accusantium doloremque laudantium, archi tecto beatae vitae dicta sunt</p>
  </div>
  <div class="news-foot"><span>03 Sep 2018</span><span>Read More</span></div>
</article>
<article class="news-card" style="left:783px">
  <div class="news-img" role="img" aria-label="Photo of colleagues applauding in a meeting" style="background:linear-gradient(150deg,#d9dde0,#aeb4b8 55%,#5e6265)"></div>
  <div class="news-body">
    <h3 class="news-cat">Publisher Portal</h3>
    <p class="news-title">Nemo enim ipsam voluptatem quia volup-<br>tas sit aspernatur aut odit</p>
    <p class="news-text">Sed ut perspiciatis unde omnis iste natus error sit vol uptatem accusantium doloremque laudantium, archi tecto beatae vitae dicta sunt</p>
  </div>
  <div class="news-foot"><span>03 Sep 2018</span><span>Read More</span></div>
</article>

<section class="banner">
  <div class="banner-art" role="img" aria-label="Photo of glowing hanging light bulbs on blue"></div>
  <h2>Sed ut perspiciatis unde</h2>
  <p>Sed ut perspiciatis unde omnis iste natus error sit voluptatem accusantium doloremque laudantium, totam rem aperiam, eaque ipsa quae ab illo invento riquasi architecto beatae vitae error sit voluptatem vitae dicta sunt explicabo qui ratione voluptatem sequi nesciunt.</p>
  <a class="btn-ghost" style="left:87px;top:284px;width:140px;height:43px;font-size:16px">Read More</a>
</section>

<footer class="site-footer">
  <div class="foot-col" style="left:101px">
    <h4>Contact Us</h4>
    <dl class="contact-lines">
      <dt>Address</dt><dd>482 Larkmoor Avenue #4B<br>Texas 75201 TX</dd>
      <dt>Phone</dt><dd>000-555-0187</dd>
      <dt>Email</dt><dd>info@quorbit.com</dd>
    </dl>
  </div>
  <div class="foot-col" style="left:361px">
    <h4>Company</h4>
    <ul class="foot-list" style="padding-left:6px"><li>Home</li><li>About Us</li><li>Services</li><li>Faq</li><li>News</li><li>Contact Us</li></ul>
  </div>
  <div class="foot-col" style="left:558px">
    <h4>Sed ut perspiciatis</h4>
    <ul class="foot-list"><li>Sed ut perspiciatis</li><li>unde omnis iste natus</li><li>error sit voluptatem</li><li>accusantium</li><li>doloremque</li><li>laudantium,</li></ul>
  </div>
  <div class="foot-col" style="left:828px"><h4>Keep in touch</h4></div>
  <div class="email-field">Email Address</div>
  <div class="subscribe">Subscribe</div>
  <span class="social" style="left:828px"></span>
  <span class="social" style="left:870px"></span>
  <span class="social" style="left:913px"></span>
  <span class="social" style="left:955px"></span>
  <span class="social" style="left:998px"></span>
  <p class="copyright">© Copyright 2018 Quorbit.All rightt reserved</p>
</footer>

</body>
</html>
```